Create a Magazine Ad for an asbestos law firm

we need an 8 X 13 ad to be on the back of a magazine cover. We have the text Attached and want a similar look and feel to our website : www.harborvale-claims.example. The ad should be targeted to white males 55 years or older who are conservative and worked in industry or industrial plants. The main offer is a free case review and trying to get them to call the telephone number.

Target Market(s)

White collar men who worked in industrial plants. Age 55 years or older.

Industry/Entity Type

Legal

Requirements
Must have
• Pictures of white middle class conservative man or man and woman
Nice to have
• look at www.harborvale-claims.example to an. idea of what we are looking for

```html
<!DOCTYPE html>
<html lang="en">
<head>
<meta charset="utf-8">
<title>Mesothelioma Compensation Ad</title>
<link href="https://fonts.googleapis.com/css2?family=Poppins:wght@400;500;600;700;800&display=swap" rel="stylesheet">
<style>
:root{
  --navy:#0f3a63;
  --navy-deep:#0b2d4f;
  --yellow:#fdb913;
  --ink:#1c2b3a;
  --paper:#ffffff;
  --mist:#eef2f6;
  --line:#c9d5e2;
}
*{box-sizing:border-box;margin:0;padding:0}
html,body{width:766px;height:1200px;overflow:hidden;background:var(--paper)}
body{font-family:'Poppins',Arial,sans-serif;color:var(--ink)}
.ad{position:relative;width:766px;height:1200px;overflow:hidden;background:var(--paper)}
.portrait{position:absolute;left:390px;top:150px;width:376px;height:500px;
  background:radial-gradient(ellipse at 55% 40%,#d9d2c8 0%,#bfb6aa 35%,#e8ecf0 75%,#f6f8fa 100%)}
.headline{position:absolute;left:40px;top:34px;width:520px;color:var(--navy);font-weight:700;line-height:1.05}
.headline .lead{font-size:34px}
.headline .disease{display:block;font-size:66px;color:var(--yellow);font-weight:800;letter-spacing:-1px;margin:4px 0 6px}
.headline .promise{font-size:36px;display:block}
.intro{position:absolute;left:40px;top:292px;width:330px;font-size:14px;line-height:1.45}
.sources{position:absolute;left:40px;top:386px;width:330px;list-style:none;font-size:14px;line-height:1.7}
.sources li::before{content:"";display:inline-block;width:7px;height:7px;border-radius:50%;background:var(--navy);margin-right:10px;vertical-align:middle}
.qualify-band{position:absolute;left:0;top:478px;width:380px;padding:9px 16px 9px 40px;background:var(--navy);color:var(--yellow);font-size:14px;font-weight:600;line-height:1.3}
.steps{position:absolute;left:40px;top:536px;width:330px;list-style:none;font-size:14px;line-height:1.35}
.steps li{display:flex;gap:10px;margin-bottom:8px}
.steps svg{flex:none;margin-top:2px}
.trust-band{position:absolute;left:0;top:652px;width:766px;height:152px;background:var(--yellow)}
.trust-title{position:absolute;left:40px;top:20px;width:340px;color:var(--navy);font-weight:700;font-size:20px;line-height:1.2}
.trust-title .amount{display:block;font-size:46px;font-weight:800;line-height:1.05}
.trust-note{position:absolute;left:400px;top:0;width:366px;height:152px;background:var(--navy);color:#fff;font-size:12.5px;line-height:1.45;padding:16px 24px}
.payouts{position:absolute;left:0;top:804px;width:766px;height:396px;background:var(--navy-deep);color:#fff}
.payouts h2{text-align:center;font-size:23px;font-weight:700;line-height:1.15;margin:18px 40px 0;text-transform:uppercase}
.payouts h2 .accent{color:var(--yellow)}
.payouts .explain{text-align:center;font-size:11.5px;line-height:1.45;margin:8px 44px 0;color:#dbe5f0}
.results{position:absolute;left:28px;top:132px;width:710px;height:132px;background:var(--paper);border-radius:6px;display:grid;grid-template-columns:repeat(6,1fr);padding:12px 10px;gap:6px}
.result{color:var(--navy);display:flex;flex-direction:column;align-items:center;text-align:center;border-right:1px solid var(--line);padding:0 4px}
.result:last-child{border-right:none}
.result .sum{font-size:15px;font-weight:800;margin-top:6px}
.result .how{font-size:10.5px;line-height:1.25;color:var(--ink);margin-top:3px}
.eligible{position:absolute;left:0;top:278px;width:766px;text-align:center;font-size:22px;font-weight:700}
.eligible .free{color:var(--yellow)}
.eligible-sub{position:absolute;left:0;top:312px;width:766px;text-align:center;font-size:12px;color:#dbe5f0}
.contact{position:absolute;left:28px;top:340px;width:710px;height:44px;display:flex;align-items:center;justify-content:space-between;border-top:1px solid rgba(255,255,255,.25);padding-top:6px}
.cta{background:var(--yellow);color:var(--navy);font-weight:700;font-size:12px;line-height:1.15;padding:7px 14px;border-radius:4px;text-transform:uppercase}
.phone{display:flex;align-items:center;gap:10px;font-size:24px;font-weight:700;color:var(--yellow)}
.firm{display:flex;align-items:center;gap:8px;font-size:11px;line-height:1.3;color:#fff}
.firm .mark{width:18px;height:18px;border-radius:50%;background:var(--yellow);flex:none}
</style>
</head>
<body>
<div class="ad">
  <div class="portrait" role="img" aria-label="Photo of a smiling older man with glasses in a light shirt"></div>

  <h1 class="headline">
    <span class="lead">Diagnosed with</span>
    <span class="disease">Mesothelioma,</span>
    <span class="promise">You could be Owed<br>Compensation</span>
  </h1>

  <p class="intro">It's very likely you developed this disease through asbestos exposure. Mesothelioma patients are getting multi-million dollar settlements, decades later, from:</p>

  <ul class="sources">
    <li>Exposure to asbestos products,</li>
    <li>Ex-employers, or</li>
    <li>Talcum baby powder companies</li>
  </ul>

  <div class="qualify-band">We can help you find out if you qualify for a case in minutes.</div>

  <ul class="steps">
    <li><svg width="14" height="14" viewBox="0 0 14 14"><path d="M2 7.5l3 3 7-7" fill="none" stroke="#0f3a63" stroke-width="2.4" stroke-linecap="round"/></svg>We'll analyze your situation at no cost</li>
    <li><svg width="14" height="14" viewBox="0 0 14 14"><path d="M2 7.5l3 3 7-7" fill="none" stroke="#0f3a63" stroke-width="2.4" stroke-linecap="round"/></svg>Determine how much compensation you could be entitled too</li>
    <li><svg width="14" height="14" viewBox="0 0 14 14"><path d="M2 7.5l3 3 7-7" fill="none" stroke="#0f3a63" stroke-width="2.4" stroke-linecap="round"/></svg>Show you the next steps to get what you're owed</li>
  </ul>

  <section class="trust-band">
    <h2 class="trust-title"><span class="amount">$30 Billion</span>is Available in Trust for Mesothelioma Patients</h2>
    <p class="trust-note">Tradesmen in many industries were negligently exposed to asbestos materials well into the 1970s. Whether you developed Mesothelioma yourself due to asbestos exposure or you're the surviving family of a lost loved one, you could be entitled to significant compensation.</p>
  </section>

  <section class="payouts">
    <h2>How much money can<br>people receive from <span class="accent">a mesothelioma case?</span></h2>
    <p class="explain">Depending on where you were exposed and a few other factors, you can get a settlement from 6 to 7 figures. Here are a few examples of Mesothelioma settlements received by our clients. These figures are the total compensation after all attorney fees and expenses are deducted.</p>

    <div class="results">
      <div class="result">
        <svg width="40" height="28" viewBox="0 0 40 28"><rect x="2" y="6" width="22" height="14" fill="none" stroke="#0f3a63" stroke-width="2"/><path d="M24 10h8l5 5v5H24z" fill="none" stroke="#0f3a63" stroke-width="2"/><circle cx="10" cy="23" r="3" fill="#0f3a63"/><circle cx="31" cy="23" r="3" fill="#0f3a63"/></svg>
        <span class="sum">$6,142,500</span><span class="how">Exposed through heavy duty vehicles</span>
      </div>
      <div class="result">
        <svg width="40" height="28" viewBox="0 0 40 28"><rect x="8" y="3" width="24" height="23" fill="none" stroke="#0f3a63" stroke-width="2"/><path d="M13 8h4M23 8h4M13 14h4M23 14h4M18 26v-6h4v6" stroke="#0f3a63" stroke-width="2" fill="none"/></svg>
        <span class="sum">$6,033,510</span><span class="how">Exposed through general contracting</span>
      </div>
      <div class="result">
        <svg width="40" height="28" viewBox="0 0 40 28"><path d="M3 16h34l-5 8H8z" fill="none" stroke="#0f3a63" stroke-width="2"/><rect x="12" y="8" width="14" height="8" fill="none" stroke="#0f3a63" stroke-width="2"/><path d="M19 8V3" stroke="#0f3a63" stroke-width="2"/></svg>
        <span class="sum">$5,939,010</span><span class="how">Exposed through boat repair</span>
      </div>
      <div class="result">
        <svg width="40" height="28" viewBox="0 0 40 28"><rect x="13" y="8" width="14" height="18" rx="3" fill="none" stroke="#0f3a63" stroke-width="2"/><rect x="16" y="2" width="8" height="6" fill="#0f3a63"/></svg>
        <span class="sum">$2.5 Million</span><span class="how">Exposed from brand-name talcum baby powder</span>
      </div>
      <div class="result">
        <svg width="40" height="28" viewBox="0 0 40 28"><circle cx="20" cy="5" r="3" fill="none" stroke="#0f3a63" stroke-width="2"/><path d="M20 8v18M13 12h14M8 18c2 6 8 8 12 8s10-2 12-8" fill="none" stroke="#0f3a63" stroke-width="2"/></svg>
        <span class="sum">$3,921,750</span><span class="how">Exposed through navy service</span>
      </div>
      <div class="result">
        <svg width="40" height="28" viewBox="0 0 40 28"><path d="M3 18h34l-5 7H8z" fill="none" stroke="#0f3a63" stroke-width="2"/><path d="M10 18V10h20v8M16 10V5h8v5" fill="none" stroke="#0f3a63" stroke-width="2"/></svg>
        <span class="sum">$3,600,450</span><span class="how">Exposed through navy service</span>
      </div>
    </div>

    <p class="eligible">Find out if you're Eligible, for <span class="free">FREE</span>, in Minutes.</p>
    <p class="eligible-sub">We'll evaluate your situation and tell you what your case could be worth.</p>

    <div class="contact">
      <span class="cta">Get your free<br>evaluation now!</span>
      <span class="phone">
        <svg width="26" height="26" viewBox="0 0 26 26"><circle cx="13" cy="13" r="13" fill="#fdb913"/><path d="M9 7l3 3-2 2c1 2 2 3 4 4l2-2 3 3-2 2c-5 0-10-5-10-10z" fill="#0b2d4f"/></svg>
        1-XXX XXXX
      </span>
      <span class="firm"><span class="mark"></span>Hartwell &amp; Pryce, LLP<br>Daniel Hartwell, Austin, TX</span>
    </div>
  </section>
</div>
</body>
</html>
```